New Web-Page Design Required

We need a new or initial web design for our page varno-labs.com. We provide products & services around infrastructure products. We have two products at the moment, but another 2 in the pipeline.
We want to have the following page structure (and part of the project is to design the 7 pages):
- Home
- Products
-One page per product
- Service
- Support
- About
- Contact (Email form)
The start page should include the following information:
- Twitter / Linkedin Links
- Telephone / Email or in general contact details
- News
- Maybe a link-box, where we can highlight/showcase things
- Link to our support portal, quite prominent
- Testimonials
It would be nice if the product pages would have a image header, where we can put up a screenshot or something. Links to datasheet and videos of the product would be nice as well.
We like the "big banner in the middle" designs, like these two Joomla examples. No need to copy them, it should just give you an idea.
http://www.plumeforge.com/itempreview/185
http://www.plumeforge.com/content/asj42/index.php
Budget for images available, so please use placeholders or ask us for specific photos/images, if you need them for your design.
Target Market(s)
Business-2-Business, Decision makers and Technical Leads
Industry/Entity Type
News
Look and feel
Each slider illustrates characteristics of the customer's brand and the style your logo design should communicate.

```html
<!DOCTYPE html>
<html lang="en">
<head>
<meta charset="utf-8">
<title>varno-labs — Home</title>
<link href="https://fonts.googleapis.com/css2?family=Roboto:wght@400;500;700;900&family=Roboto+Condensed:wght@700&display=swap" rel="stylesheet">
<style>
:root{
  --navy:#1b6482;
  --teal:#14b3c4;
  --teal-dark:#0f8ea6;
  --panel:#e6e6e6;
  --card:#ffffff;
  --ink:#222;
  --muted:#555;
  --link:#1a7fa0;
  --red:#d8101e;
}
*{box-sizing:border-box;margin:0;padding:0}
html,body{width:922px;height:1200px;overflow:hidden;background:#fff}
body{position:relative;font-family:"Roboto",Arial,sans-serif;color:var(--ink)}
.abs{position:absolute}
.page{left:16px;top:40px;width:889px;height:1110px;background:var(--panel)}
.topbar{left:13px;top:7px;width:897px;height:47px;background:var(--navy);color:#fff;font-size:11px;text-align:right;padding:22px 44px 0 0;letter-spacing:.2px}
.brand{left:53px;top:72px;display:flex;align-items:center;gap:10px}
.brand-dot{width:46px;height:46px;border-radius:50%;background:var(--navy)}
.brand-name{font-size:36px;font-weight:500;color:#555}
.search{left:736px;top:110px;width:132px;height:19px;border-radius:10px;background:#fff;border:1px solid #bbb}
.search span{position:absolute;right:3px;top:2px;height:13px;padding:0 6px;border-radius:7px;background:var(--teal-dark);color:#fff;font-size:7px;line-height:13px}
.nav{left:55px;top:139px;width:815px;height:34px;display:flex;gap:1px}
.nav a{flex:1;background:linear-gradient(#fff,#e9e9e9);border:1px solid #ddd;font-size:12px;font-weight:500;color:#555;text-align:center;line-height:34px;text-decoration:none}
.nav a.current{background:linear-gradient(#5cc8d6,var(--teal-dark));color:#fff;font-weight:700}
.nav-rule{left:53px;top:176px;width:817px;height:3px;background:var(--teal-dark)}
.banner{left:53px;top:181px;width:637px;height:231px;background:radial-gradient(ellipse at 60% 45%,#fff 0%,#ddd 70%,#bbb 100%)}
.banner-figures{position:absolute;left:105px;top:20px;width:170px;height:210px;background:linear-gradient(#bbb,#e4e4e4);border-radius:40px 40px 6px 6px;opacity:.7}
.banner h1{position:absolute;left:272px;top:56px;font-size:22px;font-weight:400;color:var(--navy)}
.banner small{position:absolute;left:356px;top:84px;font-size:8px;color:var(--link)}
.label{font-size:8px;color:#333;padding-left:18px;position:relative}
.label:before{content:"";position:absolute;left:5px;top:0;width:8px;height:8px;background:#e8561c;clip-path:polygon(0 60%,100% 0,100% 100%,0 100%)}
.news{left:53px;top:412px;width:637px;height:56px;background:#fff;border-top:1px solid #ccc}
.news .label{display:block;height:17px;line-height:17px;border-bottom:1px solid #ddd;background:#f6f6f6}
.news p{font-size:8.5px;color:#444;padding:15px 16px}
.news b{color:#e8561c;font-weight:400}
.topics{left:692px;top:181px;width:178px;height:287px;background:#fff}
.topics .label{display:block;height:19px;line-height:19px;background:#f6f6f6;border-bottom:1px solid #ddd}
.topic{position:absolute;left:14px;display:flex;gap:9px}
.topic-icon{width:50px;height:50px;border-radius:5px;background:var(--navy);display:flex;align-items:center;justify-content:center}
.topic h3{font-size:10px;font-weight:500;color:var(--link);margin-top:1px}
.topic p{font-size:7px;color:#666;line-height:8px;width:80px}
.post{left:53px;width:386px;height:142px;background:var(--card);border:1px solid #ccc}
.post-thumb{position:absolute;left:15px;top:13px;width:100px;height:102px;border:6px solid var(--navy);background:#eee}
.post h2{position:absolute;left:132px;top:13px;font-size:12.5px;font-weight:700}
.post .by{position:absolute;left:132px;top:28px;font-size:6px}
.post .body{position:absolute;left:132px;top:42px;width:240px;font-size:7px;line-height:9.4px;text-align:justify}
.post .more{position:absolute;right:14px;top:111px;font-size:7.5px;font-weight:700}
.post-meta{position:absolute;left:0;bottom:0;width:100%;height:22px;background:var(--teal);color:#fff;font-size:6.5px;line-height:22px;padding:0 16px;display:flex}
.post-meta span:first-child{flex:1}
.post-meta span+span{margin-left:14px}
.sidebar{left:452px;top:477px;width:175px;height:306px;background:#d9d9d9;border:1px solid #c4c4c4;padding:11px}
.newsletter{height:20px;border-radius:4px;background:linear-gradient(#6a6a6a,#444);color:#fff;font-size:9.5px;line-height:20px;padding-left:5px}
.side-cols{display:flex;gap:32px;margin-top:13px}
.sidebar h4{font-size:8px;font-weight:500;margin-bottom:2px}
.sidebar li{list-style:none;font-size:5.5px;line-height:9.2px}
.video{position:relative;margin-top:8px;height:92px;border-radius:6px;background:#222;padding:7px}
.video-screen{height:78px;background:#555;display:flex;align-items:center;justify-content:center}
.view-all{font-size:5.5px;text-align:right;margin-top:5px}
.tod{left:637px;top:479px;width:233px;height:196px;background:#bfbfbf;border:1px solid #aaa}
.tod h4{font-size:8.5px;font-weight:700;padding:7px 8px;color:#333}
.tod-media{position:absolute;left:8px;top:24px;width:217px;height:140px;background:#555}
.tod-caption{position:absolute;left:0;bottom:0;width:100%;height:31px;background:var(--teal);color:#fff;font-size:7px;line-height:8px;padding:5px 9px}
.popular{left:642px;top:687px;width:228px;height:96px;background:#d9d9d9;border:1px solid #aaa;padding:4px}
.popular h5{font-size:4px;margin-bottom:3px}
.pop-row{display:flex;gap:3px}
.pop-item{flex:1}
.pop-img{height:50px;background:#777}
.pop-item p{font-size:3.4px;line-height:4px;margin-top:2px}
.price{left:534px;top:826px}
.footer{left:13px;top:977px;width:897px;height:168px;background:var(--teal);color:#fff;font-size:7.5px}
.footer h3{font-size:11px;font-weight:400;margin-bottom:2px}
.footer .col{position:absolute;top:18px}
.footer li{list-style:none;line-height:12.5px}
.footer .quote{font-weight:700;line-height:9.6px;width:248px;margin-bottom:10px}
.social{display:flex;gap:44px}
.social span{width:34px;height:34px;background:#fff;opacity:.75;border-radius:4px}
.bottom{left:13px;top:1145px;width:897px;height:55px;background:var(--navy);color:#fff;font-size:8.5px;text-align:center;line-height:65px}
</style>
</head>
<body>
<div class="abs page"></div>
<header class="abs topbar">SUBSCRIBE &nbsp;|&nbsp; LOGIN</header>

<div class="abs brand"><span class="brand-dot"></span><span class="brand-name">varno-labs</span></div>
<div class="abs search"><span>Search</span></div>

<nav class="abs nav">
  <a class="current" href="#">Home</a><a href="#">Products</a><a href="#">Service</a><a href="#">Support</a><a href="#">About</a><a href="#">Contact</a>
</nav>
<div class="abs nav-rule"></div>

<section class="abs banner">
  <div class="banner-figures" role="img" aria-label="Banner photo: two business people in silhouette"></div>
  <h1>Banner in here</h1>
  <small>and more ›</small>
</section>

<section class="abs news">
  <span class="label">News</span>
  <p><b>▸</b>June 10, 2013 A new product, news of the release. &nbsp;<b>▸</b> June 10, 2013 We renewed a website.</p>
</section>

<aside class="abs topics">
  <span class="label">Topics</span>
  <div class="topic" style="top:55px"><div class="topic-icon"><svg width="30" height="30" viewBox="0 0 30 30" fill="none" stroke="#fff" stroke-width="2"><ellipse cx="15" cy="15" rx="13" ry="5"/><ellipse cx="15" cy="15" rx="13" ry="5" transform="rotate(60 15 15)"/><ellipse cx="15" cy="15" rx="13" ry="5" transform="rotate(120 15 15)"/></svg></div><div><h3>Topics01</h3><p>Topics sample text text sample Topics</p></div></div>
  <div class="topic" style="top:118px"><div class="topic-icon"><svg width="30" height="30" viewBox="0 0 30 30" fill="#fff"><path d="M14 3l2 0 1 9 10 5v2l-10-2-1 7 3 2v2l-5-1-5 1v-2l3-2-1-7-10 2v-2l10-5z" transform="rotate(-40 15 15)"/></svg></div><div><h3>Topics02</h3><p>Topics sample text text sample Topics</p></div></div>
  <div class="topic" style="top:182px"><div class="topic-icon"><svg width="30" height="30" viewBox="0 0 30 30" fill="#fff"><rect x="11" y="11" width="8" height="8" transform="rotate(45 15 15)"/><rect x="3" y="5" width="8" height="5" transform="rotate(45 7 7)"/><rect x="19" y="20" width="8" height="5" transform="rotate(45 23 22)"/></svg></div><div><h3>Topics03</h3><p>Topics sample text text sample Topics</p></div></div>
  <div class="topic" style="top:245px"><div class="topic-icon"><svg width="30" height="30" viewBox="0 0 30 30" fill="none" stroke="#fff" stroke-width="2.5"><rect x="9" y="3" width="12" height="24" rx="2" transform="rotate(35 15 15)"/></svg></div><div><h3>Topics04</h3><p>Topics sample text text sample Topics</p></div></div>
</aside>

<article class="abs post" style="top:477px"><div class="post-thumb"></div><h2>Post Title</h2><span class="by">by: admin</span><p class="body">Lorem ipsum dolor sit amet, consectetur adipiscing elit. Donec sed tellus mauris. Pellentesque nec ante vel erat tempor porttitor quis varius purus. Aenean quis odio libero, in consequat massa. Proin diam lorem, pellentesque sed fringilla hendrerit, blandit sed nisl. Ut venenatis consequat eros, at pretium tortor semper et. Sed malesuada tempor sollicitudin.</p><span class="more">Read more</span><div class="post-meta"><span>CATEGORY #1</span><span>Jan 18th, 2011</span><span>4 Comments</span></div></article>
<article class="abs post" style="top:640px"><div class="post-thumb"></div><h2>Post Title</h2><span class="by">by: admin</span><p class="body">Lorem ipsum dolor sit amet, consectetur adipiscing elit. Donec sed tellus mauris. Pellentesque nec ante vel erat tempor porttitor quis varius purus. Aenean quis odio libero, in consequat massa. Proin diam lorem, pellentesque sed fringilla hendrerit, blandit sed nisl. Ut venenatis consequat eros, at pretium tortor semper et. Sed malesuada tempor sollicitudin.</p><span class="more">Read more</span><div class="post-meta"><span>CATEGORY #1</span><span>Jan 18th, 2011</span><span>4 Comments</span></div></article>
<article class="abs post" style="top:804px"><div class="post-thumb"></div><h2>Post Title</h2><span class="by">by: admin</span><p class="body">Lorem ipsum dolor sit amet, consectetur adipiscing elit. Donec sed tellus mauris. Pellentesque nec ante vel erat tempor porttitor quis varius purus. Aenean quis odio libero, in consequat massa. Proin diam lorem, pellentesque sed fringilla hendrerit, blandit sed nisl. Ut venenatis consequat eros, at pretium tortor semper et. Sed malesuada tempor sollicitudin.</p><span class="more">Read more</span><div class="post-meta"><span>CATEGORY #1</span><span>Jan 18th, 2011</span><span>4 Comments</span></div></article>

<aside class="abs sidebar">
  <div class="newsletter">Subscribe Newsletter</div>
  <div class="side-cols">
    <div><h4>CATEGORIES</h4><ul><li>CATEGORY #1</li><li>CATEGORY #2</li><li>CATEGORY #3</li><li>CATEGORY #4</li><li>CATEGORY #5</li></ul></div>
    <div><h4>ARCHIVES</h4><ul><li>January 2013</li><li>December 2013</li><li>November 2013</li><li>October 2013</li><li>September 2013</li></ul></div>
  </div>
  <h4 style="margin-top:9px">RECENT POSTS</h4>
  <ul><li>Title Post</li><li>Title Post</li><li>Title Post</li><li>Title Post</li><li>Title Post</li></ul>
  <h4 style="margin-top:9px;padding-top:5px;border-top:1px solid #bbb">VIDEOS</h4>
  <div class="video"><div class="video-screen"><svg width="34" height="34" viewBox="0 0 34 34"><circle cx="17" cy="17" r="16" fill="#fff"/><path d="M13 10l11 7-11 7z" fill="#333"/></svg></div></div>
  <p class="view-all">View all videos</p>
</aside>

<section class="abs tod">
  <h4>Title of The Day</h4>
  <div class="tod-media" role="img" aria-label="Featured image of the day"></div>
  <div class="tod-caption"><b>Title of The Day</b><br>Lorem ipsum dolor sit amet, consectetur adipiscing elit. Donec sed tellus mauris. Pellentesque nec ante vel erat tempor...</div>
</section>

<section class="abs popular">
  <h5>Most Popular Post of The Week</h5>
  <div class="pop-row">
    <div class="pop-item"><div class="pop-img" role="img" aria-label="Post image"></div><p><b>Post Title</b><br>Lorem ipsum dolor sit amet, consectetur adipiscing elit. Donec sed tellus mauris nec ante.</p></div>
    <div class="pop-item"><div class="pop-img" role="img" aria-label="Post image"></div><p><b>Post Title</b><br>Lorem ipsum dolor sit amet, consectetur adipiscing elit. Donec sed tellus mauris nec ante.</p></div>
    <div class="pop-item"><div class="pop-img" role="img" aria-label="Post image"></div><p><b>Post Title</b><br>Lorem ipsum dolor sit amet, consectetur adipiscing elit. Donec sed tellus mauris nec ante.</p></div>
  </div>
</section>

<svg class="abs price" width="300" height="146" viewBox="0 0 300 146" aria-label="New price">
  <defs><linearGradient id="priceFill" x1="0" y1="0" x2="0" y2="1"><stop offset="0" stop-color="#f23a3a"/><stop offset="1" stop-color="#b00a14"/></linearGradient></defs>
  <path d="M4 44 L296 2 L296 110 L148 116 L136 146 L118 117 L8 122 Z" fill="url(#priceFill)"/>
  <text x="150" y="98" text-anchor="middle" font-family="'Roboto Condensed',Arial,sans-serif" font-weight="700" font-size="54" fill="#fff" transform="rotate(-6 150 70)">NEW PRICE!</text>
</svg>

<footer class="abs footer">
  <div class="col" style="left:45px"><h3>SITE NAVIGATION</h3><ul><li>Home</li><li>About</li><li>Portfolio</li><li>Blog</li><li>News</li><li>Contact Us</li></ul></div>
  <div class="col" style="left:199px"><h3>Testimonials</h3>
    <p class="quote">"Lorem ipsum dolor sit amet, consectetur adipisicing elit, sed do eiusmod tempor incididunt ut labore et dolore magna aliqua. Ut enim ad minim veniam, quis nostrud exercitation ullamco laboris nisi ut aliquip ex ea commodo consequat. Duis aute irure dolor in reprehenderit in voluptate velit esse cillum dolore eu fugiat nulla pariatur."</p>
    <p class="quote">"Lorem ipsum dolor sit amet, consectetur adipisicing elit, sed do eiusmod tempor incididunt ut labore et dolore magna aliqua. Ut enim ad minim veniam, quis nostrud exercitation ullamco laboris nisi ut aliquip ex ea commodo consequat. Duis aute irure dolor in reprehenderit in voluptate velit esse cillum dolore eu fugiat nulla pariatur."</p>
  </div>
  <div class="col" style="left:472px;width:210px;line-height:10px"><h3>WHO'S TALKIN</h3>
    <p style="font-weight:700;text-align:center;margin-bottom:3px">Most Recent Comments</p>
    <p style="margin-bottom:9px"><b>Mira Vale:</b> Lorem ipsum dolor sit amet, consectetur Donec sed tellus mauris.</p>
    <p style="margin-bottom:9px"><b>Mira Vale:</b> Lorem ipsum dolor sit amet, consectetur Donec sed tellus mauris.</p>
    <p><b>Mira Vale:</b> Lorem ipsum dolor sit amet, consectetur Donec sed tellus mauris.</p>
  </div>
  <div class="col" style="left:712px;width:160px;font-size:7px;line-height:9px">
    <div class="social"><span></span><span></span><span></span></div>
    <p style="margin-top:26px"><b>Contact us</b> for questions or problems with your BrightHollow subscription.</p>
    <p style="margin-top:8px"><b>Contact us</b> to get updates to the BrightHollow by email.</p>
  </div>
</footer>
<div class="abs bottom">Copyright © 2013 YourDomain<b>Name</b>.com. All Rights Reserved.</div>
</body>
</html>
```